Film poster for The Lanterns Kept Burning - a documentary

We need a poster for our documentary, The Lanterns Kept Burning, about how Ancient heroine Veronel finds new life in Beirut’s refugee camps, helping four Syrian women discover the strength to live with joy through the greatest of tragedies. The film is about 20% animated with the rest being vérité footage shot in Beirut, Lebanon. The title will be in Arabic and English.

Please check out our trailer here: https://www.fundmeadow.example/projects/573816402/the-lanterns-kept-burning?ref=tkzp4m

We've included some assets from the film as well as style references of other film posters we've liked.

The designer we use will also get a credit in the film.

Target Market(s)

Documentary film festivals

Industry/Entity Type

Film Production

Font styles to use
Sans Serif

Colors

Designer to choose colors to be used in the design.

Requirements
Must have
• The Title in Both English and Arabic (Can provide the text for the arabic)
• Space at the bottom to overlay film credits
Nice to have
• Include the texture of the wall and perhaps integrate both photographic and graphic imagery
Should not have
• Shouldn't be too busy - minimalistic

```html
<!DOCTYPE html>
<html lang="en">
<head>
<meta charset="utf-8">
<title>The Lanterns Kept Burning — Poster</title>
<link href="https://fonts.googleapis.com/css2?family=Amatic+SC:wght@700&family=Patrick+Hand+SC&family=Reem+Kufi:wght@600&display=swap" rel="stylesheet">
<style>
  :root {
    --poster-orange: #e4582e;
    --ink-white: #fbf4ea;
    --scarf-blue: #9bb0c6;
    --scarf-purple: #5a3a78;
    --scarf-pink: #f2b9c2;
    --scarf-teal: #1e5a5d;
    --skin-gold: #e8a640;
  }
  * { margin: 0; padding: 0; box-sizing: border-box; }
  html, body { width: 800px; height: 1200px; overflow: hidden; }
  body { background: var(--poster-orange); }
  .poster {
    position: relative;
    width: 800px;
    height: 1200px;
    background: var(--poster-orange);
    color: var(--ink-white);
    overflow: hidden;
  }
  .title {
    position: absolute;
    top: 52px;
    left: 0;
    width: 800px;
    text-align: center;
    font-family: "Amatic SC", sans-serif;
    font-weight: 700;
    line-height: 0.9;
  }
  .title-lead {
    display: block;
    font-size: 78px;
    letter-spacing: 6px;
  }
  .title-main {
    display: block;
    font-size: 122px;
    letter-spacing: 8px;
  }
  .title-arabic {
    position: absolute;
    top: 222px;
    left: 0;
    width: 800px;
    text-align: center;
    font-family: "Reem Kufi", sans-serif;
    font-weight: 600;
    font-size: 40px;
    color: var(--ink-white);
  }
  .portrait-art {
    position: absolute;
    top: 520px;
    left: 172px;
    width: 450px;
    height: 350px;
    border-radius: 46% 40% 30% 30% / 40% 40% 20% 20%;
    background: linear-gradient(90deg,
      var(--scarf-blue) 0%,
      var(--scarf-purple) 30%,
      var(--scarf-pink) 55%,
      var(--skin-gold) 72%,
      var(--scarf-teal) 100%);
  }
  .credits {
    position: absolute;
    top: 918px;
    left: 0;
    width: 800px;
    font-family: "Patrick Hand SC", sans-serif;
    font-size: 19px;
    letter-spacing: 3px;
    line-height: 25px;
  }
  .credit-row {
    display: grid;
    grid-template-columns: 383px 1fr;
    column-gap: 22px;
  }
  .credit-role { text-align: right; font-size: 15px; }
  .credit-name { text-align: left; }
</style>
</head>
<body>
<main class="poster">
  <h1 class="title">
    <span class="title-lead">THE LANTERNS</span>
    <span class="title-main">KEPT BURNING</span>
  </h1>
  <p class="title-arabic" lang="ar" dir="rtl">ظلّت الفوانيس مضاءة</p>

  <div class="portrait-art" role="img" aria-label="Illustration of four women in headscarves shown in profile, overlapping side by side, eyes closed"></div>

  <section class="credits">
    <div class="credit-row"><span class="credit-role">DIRECTORS</span><span class="credit-name">NOUR HADDAD + CELINE MARCHAND</span></div>
    <div class="credit-row"><span class="credit-role">PRODUCER</span><span class="credit-name">TOM FERRARO</span></div>
    <div class="credit-row"><span class="credit-role">CO-PRODUCER</span><span class="credit-name">DINA KARAM</span></div>
    <div class="credit-row"><span class="credit-role">EDITOR</span><span class="credit-name">DINA KARAM</span></div>
    <div class="credit-row"><span class="credit-role">DIRECTOR OF PHOTOGRAPHY</span><span class="credit-name">NOUR HADDAD + CELINE MARCHAND</span></div>
    <div class="credit-row"><span class="credit-role">COMPOSER</span><span class="credit-name">RAMIN TAVAF</span></div>
    <div class="credit-row"><span class="credit-role">ANIMATION</span><span class="credit-name">PAPERKITE</span></div>
    <div class="credit-row"><span class="credit-role">EXECUTIVE PRODUCER</span><span class="credit-name">HELEN NORCROSS</span></div>
    <div class="credit-row"><span class="credit-role">IMPACT PRODUCER</span><span class="credit-name">MIA LINDQVIST</span></div>
  </section>
</main>
</body>
</html>
```